Truck Wrap for Desk Haven Depot

We need a professionally designed truck wrap for our 26' box delivery trucks. DHD is a leading provider of new and used office furniture, workspace solutions, and architectural walls in South Florida. We have been in business 35 years. We would like to see designs with a red background on our truck wrap. Our logo is a simple stencil font. The final design should be clean an eye catching.

Target Market(s)

Businesses of all sizes

Industry/Entity Type

Commercial Office Furniture

Font styles to use
Other font styles liked:
• Stencil font for the company logo

Colors

Designer to choose colors to be used in the design.

Requirements
Must have
• Red background CMYK: 0, 90, 91, 6
Should not have
• I don't want the words overly crowded. It must be easy to read.

```html
<!DOCTYPE html>
<html lang="en">
<head>
<meta charset="utf-8">
<title>Desk Haven Depot — Truck Wrap</title>
<link href="https://fonts.googleapis.com/css2?family=Open+Sans:wght@400;600;700&family=Montserrat:wght@500;800&display=swap" rel="stylesheet">
<style>
  :root{
    --red:#e4352a;
    --black:#151515;
    --white:#ffffff;
    --page:#ffffff;
    --panel-edge:#b9b9b9;
    --office-light:#d9dee3;
    --office-mid:#aab2ba;
    --office-dark:#6f767d;
    --room-blue:#4d6677;
    --room-grey:#8a97a1;
    --room-floor:#b89a78;
  }
  *{box-sizing:border-box;margin:0;padding:0}
  html,body{width:1200px;height:980px;overflow:hidden;background:var(--page)}
  body{position:relative;font-family:"Open Sans",Arial,sans-serif;color:var(--white)}

  .panel{position:absolute;overflow:hidden;background:var(--red);border:3px solid var(--panel-edge)}

  .side-left{left:40px;top:56px;width:700px;height:346px}
  .side-right{left:40px;top:566px;width:700px;height:346px}
  .front-header{left:820px;top:66px;width:340px;height:150px}
  .rear{left:850px;top:566px;width:300px;height:346px}

  /* image column on the sides */
  .feature{position:absolute;top:0;bottom:0;width:270px;background:var(--black)}
  .side-left .feature{left:0;border-right:5px solid var(--white)}
  .side-right .feature{right:0;border-left:5px solid var(--white)}
  .feature-photo{position:absolute;left:0;right:0;top:112px;bottom:0}
  .photo-office{background:linear-gradient(135deg,var(--office-light),var(--office-mid) 55%,var(--office-dark))}
  .photo-room{background:linear-gradient(200deg,var(--room-blue),var(--room-grey) 55%,var(--room-floor))}

  /* name block */
  .brand{position:absolute}
  .brand-name{font-family:"Montserrat",Arial,sans-serif;font-weight:800;font-size:27px;line-height:29px;letter-spacing:1px;text-transform:uppercase}
  .brand-tag{font-size:11px;font-weight:400;margin-top:6px;opacity:.9}
  .feature .brand{left:22px;top:20px;right:18px}

  /* pitch block */
  .pitch{position:absolute;text-align:center}
  .pitch-kicker{font-size:15px;font-weight:400}
  .pitch-head{font-weight:600;font-size:30px;line-height:35px;text-transform:uppercase;margin-top:2px}
  .pitch-head-rule{display:flex;align-items:center;justify-content:center;gap:14px}
  .pitch-head-rule::before,.pitch-head-rule::after{content:"";width:52px;height:1.5px;background:var(--white)}
  .pitch-points{font-size:16px;line-height:22px;margin-top:12px}
  .pitch-divider{height:1px;width:330px;background:var(--white);opacity:.8;margin:16px auto 6px}
  .contacts{display:flex;justify-content:center}
  .contact{padding:0 16px}
  .contact + .contact{border-left:1px solid rgba(255,255,255,.8)}
  .contact-area{font-size:9px;font-weight:400}
  .contact-phone{font-size:19px;font-weight:700;line-height:22px}
  .web{font-family:"Montserrat",Arial,sans-serif;font-weight:500;font-size:22px;margin-top:12px}
  .web b{font-weight:800}

  .side-left .pitch{left:285px;top:30px;width:400px}
  .side-right .pitch{left:10px;top:30px;width:400px}

  /* front header */
  .front-header .brand{left:0;right:0;top:34px;text-align:center}
  .front-header .brand-name{font-size:30px;line-height:32px}

  /* rear */
  .rear-band{position:absolute;left:0;right:0;top:0;height:96px;background:var(--black);border-bottom:4px solid var(--white)}
  .rear .brand{left:0;right:0;top:16px;text-align:center}
  .rear .brand-name{font-size:24px;line-height:26px}
  .rear .brand-tag{font-size:10px;margin-top:4px}
  .rear .pitch{left:0;top:118px;width:100%}
  .rear .pitch-kicker{font-size:11px}
  .rear .pitch-head{font-size:21px;line-height:26px}
  .rear .pitch-head-rule::before,.rear .pitch-head-rule::after{width:36px}
  .rear .pitch-points{font-size:12px;line-height:16px;margin-top:6px}
  .rear .pitch-divider{width:250px;margin:10px auto 4px}
  .rear .contact{padding:0 12px}
  .rear .contact-area{font-size:7px}
  .rear .contact-phone{font-size:15px;line-height:18px}
  .rear .web{font-size:17px;margin-top:6px}
</style>
</head>
<body>

<!-- Driver side -->
<section class="panel side-left">
  <div class="feature">
    <div class="brand">
      <p class="brand-name">Desk Haven<br>Depot</p>
      <p class="brand-tag">Built for the way you work</p>
    </div>
    <div class="feature-photo photo-office" role="img" aria-label="Open-plan office with white desks and task chairs"></div>
  </div>
  <div class="pitch">
    <p class="pitch-kicker">South Florida’s Largest Selection</p>
    <h1 class="pitch-head">New &amp; Used Office<br><span class="pitch-head-rule">Furniture</span></h1>
    <p class="pitch-points">· Huge Selection &nbsp;· Everyday Low Prices<br>· Quick Professional Delivery</p>
    <div class="pitch-divider"></div>
    <div class="contacts">
      <div class="contact"><p class="contact-area">Broward/Palm Beach</p><p class="contact-phone">954-555-0142</p></div>
      <div class="contact"><p class="contact-area">Miami Dade</p><p class="contact-phone">305-555-0187</p></div>
    </div>
    <p class="web">www.<b>DHDFL</b>.com</p>
  </div>
</section>

<!-- Front header -->
<section class="panel front-header">
  <div class="brand">
    <p class="brand-name">Desk Haven Depot</p>
    <p class="brand-tag">Built for the way you work</p>
  </div>
</section>

<!-- Passenger side -->
<section class="panel side-right">
  <div class="pitch">
    <p class="pitch-kicker">South Florida’s Largest Selection</p>
    <h2 class="pitch-head">New &amp; Used Office<br><span class="pitch-head-rule">Furniture</span></h2>
    <p class="pitch-points">· Huge Selection &nbsp;· Everyday Low Prices<br>· Quick Professional Delivery</p>
    <div class="pitch-divider"></div>
    <div class="contacts">
      <div class="contact"><p class="contact-area">Broward/Palm Beach</p><p class="contact-phone">954-555-0142</p></div>
      <div class="contact"><p class="contact-area">Miami Dade</p><p class="contact-phone">305-555-0187</p></div>
    </div>
    <p class="web">www.<b>DHDFL</b>.com</p>
  </div>
  <div class="feature">
    <div class="brand">
      <p class="brand-name">Desk Haven<br>Depot</p>
      <p class="brand-tag">Built for the way you work</p>
    </div>
    <div class="feature-photo photo-room" role="img" aria-label="Glass-walled conference room with a long table and chairs"></div>
  </div>
</section>

<!-- Rear doors -->
<section class="panel rear">
  <div class="rear-band"></div>
  <div class="brand">
    <p class="brand-name">Desk Haven<br>Depot</p>
    <p class="brand-tag">Built for the way you work</p>
  </div>
  <div class="pitch">
    <p class="pitch-kicker">South Florida’s Largest Selection</p>
    <h2 class="pitch-head">New &amp; Used Office<br><span class="pitch-head-rule">Furniture</span></h2>
    <p class="pitch-points">· Huge Selection &nbsp;· Everyday Low Prices<br>· Quick Professional Delivery</p>
    <div class="pitch-divider"></div>
    <div class="contacts">
      <div class="contact"><p class="contact-area">Broward/Palm Beach</p><p class="contact-phone">954-555-0142</p></div>
      <div class="contact"><p class="contact-area">Miami Dade</p><p class="contact-phone">305-555-0187</p></div>
    </div>
    <p class="web">www.<b>DHDFL</b>.com</p>
  </div>
</section>

</body>
</html>
```